meridale partners business card

Architectural firm business card
Updates

Please note:

corporate colour black+yellow are the only elements to be kept.
NO OTHER ELEMENT TO BE REUSED FROM PREVIOUS BUSINESS CARD.
Thank you.

Dear Everyone,

Thank you for your participation. I have upload the KBSO+ logo again for incoporate in the card. in tif and pdf format.

Thank you 

I keep getting request for the logo file. Does everyone has the same problem?

I cannot do much, because the file is upload to the website server. I can't seem to see it either.

The logo file is now working. Please download. I check it myself. Thank you everyone.

Dear All,

Thank you for all the hard work. There are a lot of great work. Due to current commitment with work, I am unable to review them just yet. I will do so next week and advise everyone also. Thank you again. Best regards

Dear All,

Thank you for your participation. There are a lot of good design. Unfortunately, I can only select one. All the best. This is definitely a good crowd to work with. Thank you everyone again.

Best regards

Target Market(s)

Corporate, commercial and institutional projects only

Industry/Entity Type

Business

Requirements
Must have
• elegant simple
double sided with coating
Member of Southland Guild of Draughtsmen (logo only)
corporate colour black and

LOGO FILE UPLOADED
Should not have
• should not be the same as current business card.
upload for reference information only.
font sans serif preferred.

```html
<!DOCTYPE html>
<html lang="en">
<head>
<meta charset="utf-8">
<title>meridale partners business card</title>
<link rel="stylesheet" href="https://fonts.googleapis.com/css2?family=Open+Sans:wght@300;400;600;700&display=swap">
<style>
  :root {
    --backdrop: #3b3b3d;
    --card-orange: #f2ae50;
    --card-black: #0b0b0b;
    --ink-white: #ffffff;
    --ink-soft: #d6d6d6;
    --rule: #8a8a8a;
    --accent: #f2ae50;
  }
  * { margin: 0; padding: 0; box-sizing: border-box; }
  html, body {
    width: 1200px; height: 900px; overflow: hidden;
    background: var(--backdrop);
    font-family: "Open Sans", sans-serif;
  }
  .stage { position: relative; width: 1200px; height: 900px; }
  .card {
    position: absolute; left: 320px;
    width: 560px; height: 340px;
    box-shadow: 0 10px 30px rgba(0,0,0,.45);
  }
  .card--front { top: 90px; background: var(--card-orange); }
  .card--back { top: 470px; background: var(--card-black); }

  /* front */
  .member-badge { position: absolute; top: 18px; right: 132px; }
  .services {
    position: absolute; text-align: right;
    font-weight: 300; line-height: 1.25;
  }
  .card--front .services {
    top: 14px; right: 20px; font-size: 12px; color: var(--ink-white);
  }
  .wordmark {
    position: absolute; display: flex; align-items: baseline; gap: 8px;
    white-space: nowrap;
  }
  .wordmark__name { font-weight: 300; letter-spacing: 1px; }
  .wordmark__suffix { font-weight: 600; font-size: 11px; }
  .card--front .wordmark { left: 28px; bottom: 16px; color: var(--ink-white); }
  .card--front .wordmark__name { font-size: 52px; }

  /* back */
  .card--back .wordmark { right: 26px; top: 10px; color: var(--ink-soft); }
  .card--back .wordmark__name { font-size: 48px; }
  .card--back .wordmark__suffix { color: var(--ink-white); font-size: 10px; }
  .card--back .services {
    top: 88px; right: 26px; font-size: 14px; color: var(--ink-soft);
  }
  .accent-bar {
    position: absolute; left: 0; top: 126px;
    width: 10px; height: 42px; background: var(--accent);
  }
  .holder {
    position: absolute; left: 30px; top: 128px;
    color: var(--ink-white); white-space: nowrap;
  }
  .holder__name { font-size: 24px; font-weight: 700; }
  .holder__letters { font-size: 15px; font-weight: 300; }
  .holder__role { font-size: 15px; font-weight: 300; color: var(--accent); }
  .holder-rule {
    position: absolute; left: 30px; right: 26px; top: 168px;
    height: 1px; background: var(--rule);
  }
  .credentials, .address, .contact {
    position: absolute; color: var(--ink-soft);
    font-size: 14px; font-weight: 300; line-height: 1.4;
    white-space: nowrap;
  }
  .credentials { left: 30px; top: 174px; }
  .address { left: 30px; top: 226px; }
  .contact { left: 240px; top: 262px; }
  .label { color: var(--accent); font-weight: 600; }
  .contact__web { color: var(--accent); font-weight: 600; font-size: 15px; }
</style>
</head>
<body>
<main class="stage">
  <section class="card card--front" aria-label="Card front">
    <svg class="member-badge" width="100" height="34" viewBox="0 0 100 34" role="img" aria-label="Southland Guild of Draughtsmen member badge">
      <rect width="100" height="34" fill="#000"/>
      <rect x="36" y="3" width="60" height="28" fill="#fff"/>
    </svg>
    <p class="services">architects<br>urban designers<br>project managers</p>
    <div class="wordmark">
      <span class="wordmark__name">meridale</span>
      <span class="wordmark__suffix">partners pty limited</span>
    </div>
  </section>

  <section class="card card--back" aria-label="Card back">
    <div class="wordmark">
      <span class="wordmark__name">meridale</span>
      <span class="wordmark__suffix">partners pty limited</span>
    </div>
    <p class="services">architects<br>urban designers<br>project managers</p>

    <div class="accent-bar"></div>
    <p class="holder">
      <span class="holder__name">Linh Dao</span>
      <span class="holder__letters">kbso, mpma</span>
      <span class="holder__role">Director</span>
    </p>
    <div class="holder-rule"></div>
    <p class="credentials">Architect (reg. no. 3172)<br><span class="label">M.</span> 0400 17 42 66</p>
    <p class="address">Kestrel House<br>12 Alder Lane, Westmere<br>NSW 2199</p>

    <p class="contact">
      <span class="label">T.</span> +612 9000 4120&nbsp; <span class="label">F.</span> +612 9000 4121<br>
      <span class="label">E.</span> mail@meridalepartners.com.au<br>
      <span class="contact__web">www.meridalepartners.com.au</span>
    </p>
  </section>
</main>
</body>
</html>
```